Yoga and Wellness Center

New business- have the logo already, but wanted my cards to be more colorful.

Please find my attached logo. I am only waiting on confirmation of my
telephone number in order to have all the information right. This is for a
new yoga and wellness center in TN for a conservative audience, but I would
like a colorful business card.

Industry/Entity Type

Conservative

```html
<!DOCTYPE html>
<html lang="en">
<head>
<meta charset="utf-8">
<title>Cedar Hollow Yoga – Business Card</title>
<link rel="stylesheet" href="https://fonts.googleapis.com/css2?family=Josefin+Sans:wght@600&family=Oswald:wght@500&display=swap">
<style>
  :root {
    --backdrop: #e9e9e9;
    --card-cream: #fbf6ee;
    --navy: #1f2a5c;
    --navy-deep: #18224d;
    --orange: #dd6a2c;
    --orange-light: #ec9a62;
    --white: #ffffff;
  }
  * { margin: 0; padding: 0; box-sizing: border-box; }
  html, body {
    width: 1200px;
    height: 1169px;
    overflow: hidden;
    background: var(--backdrop);
  }
  .canvas {
    position: relative;
    width: 1200px;
    height: 1169px;
  }
  .business-card {
    position: absolute;
    left: 308px;
    top: 84px;
    width: 584px;
    height: 1000px;
    background: var(--card-cream);
    overflow: hidden;
  }
  .card-waves {
    position: absolute;
    inset: 0;
    width: 100%;
    height: 100%;
  }
  .brand-block {
    position: absolute;
    left: 0;
    right: 0;
    top: 370px;
    display: flex;
    flex-direction: column;
    align-items: center;
    gap: 34px;
  }
  .brand-dot {
    width: 150px;
    height: 150px;
    border-radius: 50%;
    background: var(--orange);
  }
  .brand-name {
    font-family: "Josefin Sans", sans-serif;
    font-weight: 600;
    font-size: 46px;
    line-height: 1.25;
    letter-spacing: 0.14em;
    color: var(--navy);
    text-align: center;
    padding-left: 0.14em;
  }
  .contact-phone {
    position: absolute;
    left: 0;
    right: 0;
    top: 888px;
    font-family: "Oswald", sans-serif;
    font-weight: 500;
    font-size: 31px;
    color: var(--white);
    text-align: center;
    letter-spacing: 0.01em;
  }
</style>
</head>
<body>
<div class="canvas">
  <div class="business-card">
    <svg class="card-waves" viewBox="0 0 330 565" preserveAspectRatio="none" aria-hidden="true">
      <defs>
        <linearGradient id="orange-sweep" x1="0" y1="0" x2="1" y2="0">
          <stop offset="0" stop-color="var(--orange)"/>
          <stop offset="1" stop-color="var(--orange-light)"/>
        </linearGradient>
        <radialGradient id="navy-glow" cx="0.5" cy="0.6" r="0.7">
          <stop offset="0" stop-color="#2a3a78"/>
          <stop offset="1" stop-color="var(--navy-deep)"/>
        </radialGradient>
      </defs>
      <!-- top accents -->
      <path class="wave-top-accent" fill="url(#orange-sweep)"
            d="M0 58 C40 74 90 80 140 76 C180 70 215 52 245 36 C205 68 160 94 110 97 C60 100 25 93 0 88 Z"/>
      <path class="wave-top-band" fill="url(#navy-glow)"
            d="M0 0 H330 V8 C250 20 185 62 120 72 C75 78 30 74 0 62 Z"/>
      <!-- bottom accents -->
      <path class="wave-bottom-accent" fill="url(#orange-sweep)"
            d="M95 440 C150 424 220 424 270 438 C300 447 320 460 330 466 V498 C300 470 250 450 200 447 C160 445 125 447 95 440 Z"/>
      <path class="wave-bottom-band" fill="url(#navy-glow)"
            d="M0 512 C60 470 150 442 225 448 C275 452 308 472 330 490 V565 H0 Z"/>
    </svg>

    <div class="brand-block">
      <div class="brand-dot"></div>
      <p class="brand-name">CEDAR HOLLOW<br>YOGA</p>
    </div>

    <p class="contact-phone">PHONE:0000-0</p>
  </div>
</div>
</body>
</html>
```